BOX DESIGN OF CANINE AND FELINE RAPID TEST with PROFESSIONAL USE

"The market is in Southeast Asia, South America, Europe, and the U.S." Clients: Veterinary clinics, pet hospitals,(a small number of home use)
Positioned as a budget-friendly yet high-performance choice
Primary colors:
Green,Orange or Blue, (select 1,or 2 color)
Neutrals: Gray, Black or White (optional)
Dimensions:158mm(L)*98mm(W)*80mm(W)

Target Market(s)

Southeast Asia, South America, Europe, and the U.S.

Colors
0054AA
0677BA
7BADD7
CADEEF
E8F1F8
0094D4
00A9DD
6FCCEA
C7EBF8
E9F6FB
00AB8E
00BBA5
67D7C9
C6EFE9
E9F9F6
59FF00
82FF00
B8FF75
E3FFCB
F4FFEA
FFC000
F8CF3A
FAE287
FDF2CF
FEFAEE
F0912C
F2A743
F7CA91
FBE8D2
FDF5EE
EE7325
F08F49
F5BC92
FAE3D3
FDF4ED

Requirements
Nice to have
• Have an attractive look and preferably have pictures of pets (or outline lines of cats and dogs)

```html
<!DOCTYPE html>
<html lang="en">
<head>
<meta charset="utf-8">
<title>Paw Probe – Canine and Feline Rapid Test Kit Box</title>
<link href="https://fonts.googleapis.com/css2?family=DM+Sans:wght@400;500;700&display=swap" rel="stylesheet">
<style>
  :root {
    --teal: #20b5a8;
    --blue: #2a60ac;
    --ink: #1a1a1a;
    --grey: #eaeaea;
    --white: #ffffff;
    --line: #3a3a3a;
    --halo: #e8f1f8;
    --halo-deep: #cadeef;
  }
  * { margin: 0; padding: 0; box-sizing: border-box; }
  html, body { width: 1200px; height: 1200px; overflow: hidden; background: var(--white); }
  body { position: relative; font-family: "DM Sans", sans-serif; color: var(--ink); }
  .dieline { position: absolute; left: 0; top: 0; width: 1200px; height: 1200px; }
  .abs { position: absolute; white-space: nowrap; }

  /* brand wordmark */
  .brand { display: flex; align-items: center; gap: 6px; font-weight: 400; letter-spacing: -0.3px; }
  .brand .dot { border: 2px solid currentColor; border-radius: 50%; flex: none; }
  .brand--lid { left: 162px; top: 285px; color: var(--white); font-size: 30px; }
  .brand--lid .dot { width: 28px; height: 28px; }
  .brand--side { left: 266px; top: 441px; color: var(--blue); font-size: 13px; }
  .brand--side .dot { width: 13px; height: 13px; border-width: 1.5px; }
  .brand--front { left: 638px; top: 429px; color: var(--blue); font-size: 21px; }
  .brand--front .dot { width: 22px; height: 22px; }

  /* side panel with contents */
  .side-title { left: 108px; top: 433px; color: var(--teal); font-weight: 700; font-size: 11.5px; }
  .side-band { left: 88px; top: 449px; width: 105px; height: 15px; background: var(--blue); color: var(--white);
    font-weight: 700; font-size: 11.5px; padding-left: 20px; line-height: 15px; }
  .contents-head { left: 108px; top: 476px; font-size: 8px; font-weight: 500; }
  .contents-list { left: 108px; top: 490px; list-style: none; font-size: 7.8px; line-height: 11.6px; white-space: normal; width: 150px; }
  .contents-list li { display: flex; gap: 5px; }
  .contents-list .num { flex: none; width: 8px; height: 8px; margin-top: 2px; border-radius: 50%; background: var(--blue);
    color: var(--white); font-size: 5px; text-align: center; line-height: 8px; }
  .storage { left: 265px; top: 474px; font-size: 6.2px; font-weight: 500; }
  .count-tag { background: var(--teal); color: var(--white); font-weight: 700; font-size: 4.6px; padding: 1px 3px; border-radius: 1px; }
  .count-tag--side { left: 265px; top: 486px; }
  .symbols { left: 266px; top: 500px; display: flex; gap: 9px; align-items: center; }
  .ivd { border: 1px solid var(--ink); font-size: 7px; padding: 0 2px; line-height: 9px; }
  .label-box { left: 266px; top: 528px; width: 121px; height: 37px; border: 1px solid var(--ink); }

  /* back panel copy */
  .back-copy { left: 434px; top: 436px; width: 170px; white-space: normal; font-size: 5.2px; line-height: 7.8px; }
  .back-copy h3 { color: var(--blue); font-size: 7px; font-weight: 500; margin-bottom: 4px; }
  .back-copy p { margin-bottom: 3px; }
  .back-copy b { font-weight: 700; }
  .back-copy .maker { color: var(--teal); font-weight: 700; margin-top: 6px; margin-bottom: 0; line-height: 8px; }

  /* front panel */
  .front-band { left: 620px; top: 474px; width: 142px; height: 21px; background: var(--teal); color: var(--white);
    font-size: 13px; font-weight: 500; line-height: 21px; padding-left: 18px; border-radius: 0 3px 3px 0; }
  .front-title { left: 639px; top: 497px; color: var(--blue); font-size: 16.5px; font-weight: 700; }
  .front-tagline { left: 639px; top: 520px; color: var(--teal); font-size: 6.6px; }
  .features { left: 637px; top: 545px; display: flex; gap: 7px; }
  .feature { display: flex; align-items: center; gap: 3px; color: var(--blue); font-size: 4.8px; font-weight: 500; line-height: 5.4px; }
  .feature .ico { width: 14px; height: 14px; border-radius: 50%; background: var(--teal); flex: none; }
  .count-tag--front { left: 897px; top: 550px; background: var(--blue); font-size: 4.6px; }
  .pets-photo { left: 786px; top: 428px; width: 167px; height: 145px;
    background: linear-gradient(100deg, #9c8a74 0%, #5e5347 35%, #2b2420 60%, #b07a45 80%, #3a2f28 100%);
    clip-path: polygon(0 100%, 10% 40%, 30% 38%, 55% 8%, 100% 2%, 100% 100%); }

  /* brand strip */
  .swatch { position: absolute; }
  .swatch--light { left: 0; top: 864px; width: 532px; height: 168px; background: var(--grey); }
  .swatch--blue-row { left: 0; top: 1032px; width: 532px; height: 168px; background: var(--blue); }
  .swatch--teal { left: 532px; top: 864px; width: 335px; height: 336px; background: var(--teal); }
  .swatch--blue { left: 867px; top: 864px; width: 333px; height: 336px; background: var(--blue); }
  .brand--strip { font-size: 68px; gap: 26px; }
  .brand--strip .dot { width: 62px; height: 62px; border-width: 5px; }
  .brand--on-grey { left: 68px; top: 905px; color: var(--blue); }
  .brand--on-blue { left: 68px; top: 1073px; color: #ececec; }
  .brand--tile { color: var(--white); font-size: 34px; gap: 14px; }
  .brand--tile .dot { width: 34px; height: 34px; border-width: 3.5px; }
  .brand--on-teal { left: 570px; top: 1010px; }
  .brand--on-blue-tile { left: 905px; top: 1010px; }
</style>
</head>
<body>

<svg class="dieline" viewBox="0 0 1200 1200" xmlns="http://www.w3.org/2000/svg" fill="none" stroke="var(--line)" stroke-width="0.8">
  <!-- lid -->
  <path d="M88,407 V186 Q88,161 113,161 H391 Q416,161 416,186 V407 Z" fill="var(--teal)"/>
  <line x1="88" y1="203" x2="416" y2="203"/>
  <!-- glue flap -->
  <path d="M88,407 L46,413 V567 L88,573"/>
  <!-- body panels -->
  <rect x="88" y="407" width="1064" height="166" fill="var(--white)"/>
  <line x1="416" y1="407" x2="416" y2="573"/>
  <line x1="620" y1="407" x2="620" y2="573"/>
  <line x1="948" y1="407" x2="948" y2="573"/>
  <!-- top tucks -->
  <path d="M416,407 L421,402 V314 H590 Q609,314 609,333 L615,398 L620,402 V407"/>
  <path d="M948,407 L952,402 L957,333 Q959,314 978,314 H1147 V402 L1152,407"/>
  <!-- bottom flaps -->
  <path d="M88,573 V717 H143 Q159,717 159,701 V675 H345 V701 Q345,717 361,717 H416 V573"/>
  <path d="M416,573 L518,643 V669 Q518,686 534,686 H620 V573"/>
  <path d="M620,573 L691,674 V701 Q691,717 706,717 H862 Q877,717 877,701 V674 L948,573"/>
  <path d="M948,573 V686 H1034 Q1050,686 1050,669 V643 L1152,573"/>
  <!-- front halo -->
  <clipPath id="band-clip"><rect x="620" y="407" width="328" height="166"/></clipPath>
  <g clip-path="url(#band-clip)" stroke="none">
    <circle cx="876" cy="519" r="102" fill="var(--halo)"/>
    <circle cx="876" cy="519" r="80" fill="#dcebf4"/>
    <circle cx="876" cy="519" r="58" fill="#c8ebe6"/>
  </g>
  <!-- circular seal on end panel -->
  <path id="seal-ring" d="M1048,528 A37,37 0 1,1 1048.1,528" stroke="none"/>
  <text font-family="DM Sans, sans-serif" font-size="9" fill="var(--blue)" stroke="none" letter-spacing="0.6">
    <textPath href="#seal-ring" startOffset="3%">Trusted by Vets,  Loved by Pets</textPath>
  </text>
  <circle cx="1048" cy="491" r="14" stroke="var(--teal)" stroke-width="1.6"/>
  <text x="1048" y="493" text-anchor="middle" font-family="DM Sans, sans-serif" font-size="5" fill="var(--teal)" stroke="none">Paw Probe</text>
  <!-- storage symbols -->
  <g stroke="var(--ink)" stroke-width="1">
    <line x1="302" y1="503" x2="302" y2="516"/>
    <circle cx="302" cy="517" r="2" fill="var(--ink)"/>
    <line x1="302" y1="503" x2="308" y2="503"/>
    <circle cx="323" cy="505" r="3"/>
    <path d="M318,518 L326,511 L334,518 Z"/>
    <rect x="344" y="504" width="16" height="13"/>
    <circle cx="356" cy="506" r="4" fill="var(--white)"/>
    <circle cx="379" cy="510" r="7.5"/>
    <line x1="374" y1="515" x2="384" y2="505"/>
  </g>
</svg>

<!-- lid -->
<div class="abs brand brand--lid"><span class="dot"></span>Paw Probe</div>

<!-- side panel -->
<div class="abs side-title">Canine and Feline</div>
<div class="abs side-band">Rapid Test Kit</div>
<div class="abs contents-head">Contents</div>
<ol class="abs contents-list">
  <li><span class="num">1</span><span>Test Kits(Cassette,disposable dropper,desiccant).</span></li>
  <li><span class="num">2</span><span>Assay buffer.</span></li>
  <li><span class="num">3</span><span>Sterile swabs.</span></li>
  <li><span class="num">4</span><span>Instruction manual.</span></li>
</ol>
<div class="abs brand brand--side"><span class="dot"></span>Paw Probe</div>
<div class="abs storage">Store at 2~30°C, Avoid direct sunlight</div>
<div class="abs count-tag count-tag--side">10 Tests/Box</div>
<div class="abs symbols"><span class="ivd">IVD</span></div>
<div class="abs label-box"></div>

<!-- back panel -->
<div class="abs back-copy">
  <h3>Paw Probe Rapid Test</h3>
  <p><b>Simple &amp; Convenient:</b> No professional skills required,Simple enough for home use.</p>
  <p><b>Fast &amp; Efficient:</b> Digital results in &lt; 10 minutes - from start to completion.</p>
  <p><b>Accurate &amp; Reliable:</b> Quick and trustworthy pet health results using advanced lateral flowbiotech,Trusted by vet clinics worldwide.</p>
  <p>Supports screening of multiple diseases, Helping pet owners detect issues early.</p>
  <p class="maker">MADE by NORAVET™<br>Loved by Pets, Trusted by Vets</p>
</div>

<!-- front panel -->
<div class="abs brand brand--front"><span class="dot"></span>Paw Probe</div>
<div class="abs front-band">Canine and Feline</div>
<div class="abs front-title">Rapid Test Kit</div>
<div class="abs front-tagline">Loved by Pets, Trusted by Vets</div>
<div class="abs features">
  <div class="feature"><span class="ico"></span><span>Results in<br>10 Min</span></div>
  <div class="feature"><span class="ico"></span><span>Health Check<br>for Dog and Cat</span></div>
  <div class="feature"><span class="ico"></span><span>EASY<br>TO USE</span></div>
</div>
<div class="abs pets-photo" role="img" aria-label="Photo of a tabby cat and a tricolour dog sitting side by side"></div>
<div class="abs count-tag count-tag--front">10 Tests/Box</div>

<!-- brand strip -->
<div class="swatch swatch--light"></div>
<div class="swatch swatch--blue-row"></div>
<div class="swatch swatch--teal"></div>
<div class="swatch swatch--blue"></div>
<div class="abs brand brand--strip brand--on-grey"><span class="dot"></span>Paw Probe</div>
<div class="abs brand brand--strip brand--on-blue"><span class="dot"></span>Paw Probe</div>
<div class="abs brand brand--tile brand--on-teal"><span class="dot"></span>Paw Probe</div>
<div class="abs brand brand--tile brand--on-blue-tile"><span class="dot"></span>Paw Probe</div>

</body>
</html>
```